Business Card Design

We need a business card design for our new expansion based in Bloomfield Hills, Michigan. Our company is Quiet Harbor Institute & Wellness Center. Our Academy teaches individuals of all ages and professions to live from their soul. We teach intuitive development, meditation and mindfulness; shamanic healing. And ourr healing center provides holistic services. We offer certification programs that support the ethical practices of Intuitive professionals. Our team of Intuitive Practitioners includes: doctors, psychologists, chiropractor, soul retrievers, mediums, etc who all balance their knowledge with intuitive wisdom.

We want our symbol to be the Blue Morpho Buttefly and the colors on the card to complement it. We want to communicate inspiration, healing and empowerment. Thank you
Updates

Industry/Entity Type

Business

Contact Information for Business Card

Dana Orwick
Medium. Author. Soul Retriever.
Founder, Quiet Harbor

Quiet Harbor

19 North Cedar Mill Drive Suite 100
Fernwood Heights, MI 48517
248-603-7418

www.danaorwick.example

Requirements
Must have
• blue morpho butterfly

```html
<!DOCTYPE html>
<html lang="en">
<head>
<meta charset="UTF-8">
<title>Quiet Harbor — Business Card</title>
<link href="https://fonts.googleapis.com/css2?family=Lato:wght@400;700;900&display=swap" rel="stylesheet">
<style>
  :root {
    --page-bg: #e9ecef;
    --card-white: #ffffff;
    --card-mist: #e3f0fb;
    --sky-light: #c6e2f6;
    --sky-frame: #94c9ee;
    --band-blue: #3a86cc;
    --accent-blue: #2f7fc8;
    --morpho-deep: #1f63c6;
    --morpho-bright: #3fa6f0;
    --ink: #1c1d20;
    --ink-soft: #3a3c40;
    --divider: #c9d3dc;
  }
  * { box-sizing: border-box; margin: 0; padding: 0; }
  html, body {
    width: 1200px;
    height: 926px;
    overflow: hidden;
  }
  body {
    background: var(--page-bg);
    font-family: "Lato", "Helvetica Neue", Arial, sans-serif;
    color: var(--ink);
    display: flex;
    align-items: center;
    justify-content: center;
    gap: 44px;
  }

  .card {
    position: relative;
    width: 540px;
    height: 310px;
    overflow: hidden;
    box-shadow: 0 8px 24px rgba(30, 40, 55, 0.18);
  }

  /* Butterfly artwork area */
  .butterfly-art {
    background: radial-gradient(ellipse at 50% 50%, var(--morpho-bright) 0%, var(--morpho-deep) 55%, rgba(31, 99, 198, 0) 72%);
  }

  .wordmark {
    font-weight: 900;
    text-transform: uppercase;
    color: var(--ink);
    letter-spacing: -0.5px;
    white-space: nowrap;
  }

  /* ---------- Contact side ---------- */
  .card--contact {
    background: linear-gradient(160deg, var(--card-white) 0%, var(--card-white) 35%, var(--card-mist) 100%);
  }
  .card--contact .brand {
    position: absolute;
    left: 0;
    top: 34px;
    width: 240px;
    display: flex;
    flex-direction: column;
    align-items: center;
  }
  .card--contact .butterfly-art {
    width: 150px;
    height: 112px;
  }
  .card--contact .wordmark {
    margin-top: 26px;
    font-size: 23px;
  }
  .card--contact .divider {
    position: absolute;
    left: 248px;
    top: 54px;
    width: 1px;
    height: 190px;
    background: linear-gradient(to bottom, rgba(201, 211, 220, 0), var(--divider) 25%, var(--divider) 75%, rgba(201, 211, 220, 0));
  }
  .details {
    position: absolute;
    left: 268px;
    top: 48px;
    right: 16px;
  }
  .details .name {
    font-size: 19px;
    font-weight: 900;
    color: var(--ink);
  }
  .details .role {
    font-size: 12px;
    font-weight: 900;
    color: var(--accent-blue);
    margin-left: 3px;
  }
  .details .tagline {
    font-size: 11.5px;
    color: var(--ink-soft);
    margin-top: 4px;
  }
  .details .address {
    font-size: 12.5px;
    line-height: 1.35;
    color: var(--ink-soft);
    margin-top: 24px;
    font-style: normal;
  }
  .contact-line {
    display: flex;
    align-items: center;
    gap: 7px;
    font-size: 17px;
    color: var(--ink);
    margin-top: 14px;
  }
  .contact-line + .contact-line { margin-top: 8px; }
  .contact-line svg { width: 15px; height: 15px; fill: var(--accent-blue); flex: none; }
  .card--contact .band {
    position: absolute;
    left: 0;
    right: 0;
    bottom: 0;
    height: 26px;
    background: var(--band-blue);
  }

  /* ---------- Logo side ---------- */
  .card--logo {
    background: var(--sky-frame);
    padding: 10px;
  }
  .card--logo .panel {
    width: 100%;
    height: 100%;
    background: radial-gradient(ellipse at 50% 35%, #f3f9fe 0%, #dcedfa 40%, var(--sky-light) 100%);
    display: flex;
    flex-direction: column;
    align-items: center;
    padding-top: 36px;
  }
  .card--logo .butterfly-art {
    width: 180px;
    height: 134px;
  }
  .card--logo .wordmark {
    margin-top: 24px;
    font-size: 29px;
  }
</style>
</head>
<body>

  <section class="card card--contact" aria-label="Business card, contact side">
    <div class="brand">
      <div class="butterfly-art" role="img" aria-label="Blue morpho butterfly emblem"></div>
      <div class="wordmark">Quiet Harbor</div>
    </div>
    <div class="divider"></div>
    <div class="details">
      <p><span class="name">Dana Orwick</span><span class="role">-AUTHOR</span></p>
      <p class="tagline">Medium. Author. Soul Retriever.</p>
      <address class="address">
        19 North Cedar Mill Drive<br>
        Suite 100 Fernwood Heights<br>
        MI 48517
      </address>
      <p class="contact-line">
        <svg viewBox="0 0 24 24" aria-hidden="true"><path d="M4 9c0-2 2-4 8-4s8 2 8 4v1.5c0 .6-.5 1-1 1h-3c-.6 0-1-.4-1-1V9.5c-1-.4-2-.5-3-.5s-2 .1-3 .5v1c0 .6-.4 1-1 1H5c-.5 0-1-.4-1-1V9zm3 4h10l2 6H5l2-6zm5 1.5a2 2 0 1 0 0 4 2 2 0 0 0 0-4z"/></svg>
        248-603-7418
      </p>
      <p class="contact-line">
        <svg viewBox="0 0 24 24" aria-hidden="true"><path d="M2 4h20v13H2V4zm2 2v9h16V6H4zm5 12h6v2H9v-2z"/></svg>
        www.danaorwick.example
      </p>
    </div>
    <div class="band"></div>
  </section>

  <section class="card card--logo" aria-label="Business card, logo side">
    <div class="panel">
      <div class="butterfly-art" role="img" aria-label="Blue morpho butterfly emblem"></div>
      <div class="wordmark">Quiet Harbor</div>
    </div>
  </section>

</body>
</html>
```